Stationary Design needed for luxorious bespoke tailor

We need a design for our stationary items like businescards, letters, envelope and letter head / Signature for email. Our company "VELMARDO" sells exclusively and luxourious bespoke garments and accessories for men. The desgins of letterhead, envelope and business card shoulderstand communicate luxury, high quality and good taste. We would like our logo to be used on the designs.

Target Market(s)

Gentleman with a high aproach and exclusive and luxourious suits and shirts, grooms, businesman,

Industry/Entity Type

It Company

Font styles to use
Sans Serif

Colors
ec1f27
ffffff

Requirements
Must have
• Logo, Companies name and adress, contactName internet & email, phone number line / mobile, VAT Nr. On Business Card frontpage only logo and name, adress companies on backpage. No VAT and Companies ID there. Company data; VELMARDO AG Sonnwiesweg 27 4068 Basel Switzerland VAT: CHE 472 916 503 Tax Tel 41 61 508 37 14 Mobile 41 79 842 07 91 www.velmardo.ch info@velmardo.com.
Nice to have
• -Name And phone numbers need to be able to change (for different coworkers ...)
Should not have
• no VAT in Business Card

```html
<!DOCTYPE html>
<html lang="de">
<head>
<meta charset="utf-8">
<title>VELMARDO – Visitenkarte</title>
<link rel="stylesheet" href="https://fonts.googleapis.com/css2?family=Open+Sans:wght@400;600&display=swap">
<style>
  :root {
    --brand-red: #ec1f27;
    --paper: #ffffff;
    --ink: #1a1a1a;
    --card-black: #070505;
    --backdrop: #5b5b5b;
  }
  * { margin: 0; padding: 0; box-sizing: border-box; }
  html, body {
    width: 1200px; height: 1200px; overflow: hidden;
    background: var(--backdrop);
    font-family: "Open Sans", sans-serif;
  }
  .card {
    position: absolute;
    left: 283px;
    width: 634px;
    height: 360px;
  }
  .card--front { top: 212px; background: var(--paper); color: var(--ink); }
  .card--back { top: 629px; background: var(--card-black); }

  .wordmark {
    position: absolute;
    font-weight: 600;
    letter-spacing: 0.04em;
    line-height: 1;
    white-space: nowrap;
  }
  .card--front .wordmark {
    right: 30px; top: 40px;
    font-size: 40px; color: var(--ink);
  }
  .card--back .wordmark {
    left: 0; right: 0; top: 152px;
    text-align: center;
    font-size: 56px; color: var(--paper);
  }

  .person { position: absolute; left: 37px; top: 124px; }
  .person__name { font-size: 23px; color: var(--brand-red); line-height: 1.2; }
  .person__role { font-size: 14.5px; line-height: 1.4; }

  .divider { position: absolute; left: 0; top: 0; width: 634px; height: 360px; }

  .contact-list {
    position: absolute; left: 34px; top: 235px;
    list-style: none; font-size: 15.5px; line-height: 21.3px;
  }
  .contact-list li { display: flex; align-items: center; gap: 8px; }
  .contact-list svg { width: 16px; height: 16px; flex: none; }

  .address {
    position: absolute; right: 37px; top: 235px;
    text-align: right; font-style: normal;
    font-size: 15.5px; line-height: 21.3px;
  }
</style>
</head>
<body>

<section class="card card--front" aria-label="Visitenkarte Vorderseite">
  <div class="wordmark">VELMARDO</div>

  <div class="person">
    <p class="person__name">Lukas Brenner</p>
    <p class="person__role">Managing Partner</p>
  </div>

  <svg class="divider" viewBox="0 0 634 360" aria-hidden="true">
    <polyline points="0,198 226,198 326,326" fill="none" stroke="#1a1a1a" stroke-width="1.2"/>
    <polyline points="0,207 222,207 322,334 634,334" fill="none" stroke="var(--brand-red)" stroke-width="1.2"/>
  </svg>

  <ul class="contact-list">
    <li>
      <svg viewBox="0 0 16 16" aria-hidden="true"><path d="M1 6c0-3 3-4 7-4s7 1 7 4l-3 1-1-2H5L4 7z" fill="var(--brand-red)"/><path d="M3 8l2-2h6l2 2v6H3z" fill="var(--brand-red)"/><circle cx="8" cy="10.5" r="1.8" fill="#fff"/></svg>
      +41 61 508 37 14
    </li>
    <li>
      <svg viewBox="0 0 16 16" aria-hidden="true"><rect x="4" y="1" width="8" height="14" rx="1.5" fill="none" stroke="var(--brand-red)" stroke-width="1.4"/><circle cx="8" cy="12.6" r="0.9" fill="var(--brand-red)"/></svg>
      +41 79 842 07 91
    </li>
    <li>
      <svg viewBox="0 0 16 16" aria-hidden="true"><rect x="1" y="3" width="14" height="10" fill="var(--brand-red)"/><polyline points="1,3 8,9 15,3" fill="none" stroke="#fff" stroke-width="1.2"/></svg>
      info@velmardo.com
    </li>
    <li>
      <svg viewBox="0 0 16 16" aria-hidden="true" fill="none" stroke="var(--brand-red)" stroke-width="1"><circle cx="8" cy="8" r="6.5"/><ellipse cx="8" cy="8" rx="3" ry="6.5"/><line x1="1.5" y1="8" x2="14.5" y2="8"/><line x1="2.5" y1="4.5" x2="13.5" y2="4.5"/><line x1="2.5" y1="11.5" x2="13.5" y2="11.5"/></svg>
      www.velmardo.ch
    </li>
  </ul>

  <address class="address">
    VELMARDO AG<br>
    Sonnwiesweg 27<br>
    4068 Basel<br>
    Switzerland
  </address>
</section>

<section class="card card--back" aria-label="Visitenkarte Rückseite">
  <div class="wordmark">VELMARDO</div>
</section>

</body>
</html>
```